Salon and Spa Distributor Business Card

Need a business card. We are are distributor in the salon and spa industry. We identify with natural beauty. Need a card with:
Company Name: Petal Harbor"
Title: "President & CEO"
Address
Company Phone number
email
website
Tag Line:" The Professional Salon Source"

Industry/Entity Type

Business

Contact Information for Business Card

Name: Leo Mendoza
Title: "President & CEO"
Address: 317 Birchline Ave, Westbrook, NJ 08412
Company Phone number: 800-463-5108
email: leomendoza@petalharbor-example.com
website: www.petalharbor-example.com

Requirements
Should not have
• No black backgrounds

```html
<!DOCTYPE html>
<html lang="en">
<head>
<meta charset="utf-8">
<title>Petal Harbor – Business Card</title>
<link rel="stylesheet" href="https://fonts.googleapis.com/css2?family=Questrial&family=PT+Sans:wght@400;700&display=swap">
<style>
  :root {
    --backdrop: #e8e8e4;
    --card-white: #ffffff;
    --brand-green: #3f9e3c;
    --name-green: #1f7f36;
    --icon-green: #2a8a3a;
    --muted-grey: #8a8a8a;
    --body-grey: #4a4a4a;
    --back-light: #5db848;
    --back-mid: #2f9640;
    --back-dark: #0f6e33;
    --on-green: #ffffff;
  }
  * { box-sizing: border-box; margin: 0; padding: 0; }
  html, body { width: 1200px; height: 987px; overflow: hidden; }
  body { background: var(--backdrop); position: relative; font-family: "PT Sans", sans-serif; }

  .card {
    position: absolute;
    width: 615px;
    height: 352px;
    box-shadow: 0 3px 10px rgba(0,0,0,0.18);
    overflow: hidden;
  }
  .card-front { left: 293px; top: 130px; background: var(--card-white); }
  .card-back {
    left: 292px; top: 506px; height: 350px;
    background: radial-gradient(ellipse 60% 65% at 48% 42%, var(--back-light) 0%, var(--back-mid) 55%, var(--back-dark) 100%);
  }

  .brand-dot { position: absolute; border-radius: 50%; }
  .card-front .brand-dot { left: 64px; top: 56px; width: 96px; height: 96px; background: var(--brand-green); }
  .card-back .brand-dot { left: 128px; top: 130px; width: 96px; height: 96px; background: var(--on-green); }

  .wordmark {
    position: absolute;
    font-family: "Questrial", sans-serif;
    font-size: 35px;
    line-height: 1;
    white-space: nowrap;
  }
  .card-front .wordmark { left: 179px; top: 86px; color: var(--brand-green); }
  .card-back .wordmark { left: 253px; top: 166px; color: var(--on-green); }

  .tagline {
    position: absolute; left: 257px; top: 204px;
    color: var(--on-green); font-size: 17px; white-space: nowrap;
  }

  .holder { position: absolute; left: 186px; top: 153px; }
  .holder-name { color: var(--name-green); font-weight: 700; font-size: 22px; line-height: 1.1; }
  .holder-title { color: var(--muted-grey); font-size: 16px; margin-top: 2px; }

  .contact-list { position: absolute; left: 186px; top: 216px; list-style: none; }
  .contact-list li {
    display: flex; align-items: center; gap: 8px;
    color: var(--body-grey); font-size: 16px; height: 24px;
  }
  .contact-list svg { width: 15px; height: 15px; flex: none; fill: var(--icon-green); }
  .address { position: absolute; left: 186px; top: 290px; color: var(--body-grey); font-size: 16px; }
</style>
</head>
<body>

<section class="card card-front" aria-label="Business card front">
  <span class="brand-dot"></span>
  <div class="wordmark">Petal Harbor</div>

  <div class="holder">
    <p class="holder-name">Petal Harbor</p>
    <p class="holder-title">President &amp; CEO</p>
  </div>

  <ul class="contact-list">
    <li>
      <svg viewBox="0 0 16 16" aria-hidden="true"><path d="M3.6 1.2l2.3 2.6-1.4 1.6c.9 2 2.3 3.4 4.2 4.3l1.6-1.4 2.6 2.3-1.2 2.3C7 12.6 3.4 9 1.3 2.4z"/></svg>
      800-463-5108
    </li>
    <li>
      <svg viewBox="0 0 16 16" aria-hidden="true"><path d="M1 3.5h14v9H1z M1.6 4l6.4 5 6.4-5" fill="none" stroke="#2a8a3a" stroke-width="0"/><rect x="1" y="3.5" width="14" height="9" rx="1"/><path d="M1.5 4.2L8 9l6.5-4.8" fill="none" stroke="#fff" stroke-width="1.3"/></svg>
      leomendoza@petalharbor-example.com
    </li>
    <li>
      <svg viewBox="0 0 16 16" aria-hidden="true"><circle cx="8" cy="8" r="7"/><path d="M1.5 8h13M8 1c-2.5 3-2.5 11 0 14M8 1c2.5 3 2.5 11 0 14" fill="none" stroke="#fff" stroke-width="1.1"/></svg>
      www.petalharbor-example.com
    </li>
  </ul>
  <p class="address">317 Birchline Ave, Westbrook, NJ 08412</p>
</section>

<section class="card card-back" aria-label="Business card back">
  <span class="brand-dot"></span>
  <div class="wordmark">Petal Harbor</div>
  <p class="tagline">The Professional Salon Source</p>
</section>

</body>
</html>
```